Refresh of The Marston Collective business card

Update business card design using existing primary logo. Names, numbers, etc. are too hard to read on current design.

Target Market(s)

We are a CPA firm.

Industry/Entity Type

Accountant

Contact Information for Business Card

update current card

Colors
0355a3
3176b5
85acd3
0792cd

Requirements
Must have
• Easier to read phone numbers and names
• Use existing logo
Nice to have
• We love our color scheme and current TMC logo. But the names and phone numbers are too small and card just look old and stale.

```html
<!DOCTYPE html>
<html lang="en">
<head>
<meta charset="utf-8">
<title>The Marston Collective – Business Card</title>
<link rel="stylesheet" href="https://fonts.googleapis.com/css2?family=Cinzel:wght@500&family=Montserrat:wght@400;500&display=swap">
<style>
  :root {
    --backdrop: #1c1c1e;
    --navy: #24397a;
    --navy-deep: #1b2c63;
    --brand-blue: #0355a3;
    --white: #ffffff;
    --ink: #2b2b33;
    --rule: #9aa3bd;
  }
  * { box-sizing: border-box; margin: 0; padding: 0; }
  html, body { width: 1200px; height: 929px; overflow: hidden; }
  body {
    background: var(--backdrop);
    font-family: "Montserrat", sans-serif;
    position: relative;
  }
  .card {
    position: absolute;
    left: 290px;
    width: 620px;
    height: 354px;
    border-radius: 18px;
    overflow: hidden;
  }
  .card--front { top: 70px; background: linear-gradient(135deg, var(--navy) 0%, var(--navy-deep) 100%); }
  .card--back { top: 494px; background: var(--white); }

  .brand { position: absolute; display: flex; align-items: center; gap: 18px; }
  .brand__disc {
    flex: none;
    border-radius: 50%;
  }
  .brand__name {
    font-family: "Cinzel", serif;
    font-weight: 500;
    line-height: 1.05;
  }

  .card--front .brand { left: 150px; top: 108px; }
  .card--front .brand__disc { width: 96px; height: 96px; border: 3px solid var(--white); }
  .card--front .brand__name { color: var(--white); font-size: 36px; }

  .website {
    position: absolute;
    left: 0; right: 0; bottom: 58px;
    text-align: center;
    color: var(--white);
    font-size: 17px;
    letter-spacing: 0.5px;
  }

  .card--back .brand { right: 34px; top: 30px; gap: 12px; }
  .card--back .brand__disc { width: 66px; height: 66px; background: var(--brand-blue); border: 3px solid var(--navy-deep); }
  .card--back .brand__name { color: var(--navy); font-size: 22px; }

  .name-band {
    position: absolute;
    left: 0; top: 120px;
    width: 400px; height: 78px;
    background: var(--navy);
    clip-path: polygon(0 0, 100% 0, 92% 100%, 0 100%);
    color: var(--white);
    padding: 14px 0 0 30px;
  }
  .name-band__name { font-family: "Cinzel", serif; font-weight: 500; font-size: 22px; letter-spacing: 0.5px; }
  .name-band__title { font-size: 17px; margin-top: 2px; }

  .contacts {
    position: absolute;
    left: 30px; bottom: 34px;
    list-style: none;
    color: var(--ink);
    font-size: 16px;
  }
  .contacts li { display: flex; align-items: center; gap: 12px; line-height: 26px; }
  .contacts svg { width: 14px; height: 14px; fill: var(--navy); flex: none; }

  .address {
    position: absolute;
    right: 34px; top: 228px;
    text-align: right;
    color: var(--ink);
    font-size: 16px;
    line-height: 24px;
  }
</style>
</head>
<body>
  <section class="card card--front">
    <div class="brand">
      <span class="brand__disc"></span>
      <span class="brand__name">The Marston<br>Collective</span>
    </div>
    <p class="website">www.marstoncollective.com</p>
  </section>

  <section class="card card--back">
    <div class="name-band">
      <p class="name-band__name">NATHAN P. MARSTON, CPA</p>
      <p class="name-band__title">Founder</p>
    </div>
    <div class="brand">
      <span class="brand__disc"></span>
      <span class="brand__name">The Marston<br>Collective</span>
    </div>
    <p class="address">120 Harbor Ln. Suite<br>310 Lakeview, Florida 30000</p>
    <ul class="contacts">
      <li>
        <svg viewBox="0 0 16 16" aria-hidden="true"><path d="M3 1l3 3-1.6 2a9 9 0 0 0 5.6 5.6L12 10l3 3-2 2C6.5 15 1 9.5 1 3z"/></svg>
        555.210.4836
      </li>
      <li>
        <svg viewBox="0 0 16 16" aria-hidden="true"><path d="M4 0h8a1 1 0 0 1 1 1v14a1 1 0 0 1-1 1H4a1 1 0 0 1-1-1V1a1 1 0 0 1 1-1zm1 2v10h6V2z"/></svg>
        555.210.4837
      </li>
      <li>
        <svg viewBox="0 0 16 16" aria-hidden="true"><path d="M4 1h8v4H4zM1 6h14v6h-3v3H4v-3H1zm5 5v2h4v-2z"/></svg>
        555.210.4838
      </li>
      <li>
        <svg viewBox="0 0 16 16" aria-hidden="true"><path d="M1 3h14v10H1zm1.5 1.5L8 9l5.5-4.5z" fill-rule="evenodd"/></svg>
        nathan@marstoncollective.com
      </li>
    </ul>
  </section>
</body>
</html>
```